Business Card Design Project for Heron Lending

Hello there,

We are looking for a business card design for our new Heron Lending car financing company. We are looking for a business card that will include:

- An address
- Telephone number and extension
- Employee Name
- Employee Title
- Our logo and name clearly visible

We are including our logo with this writeup, we are looking to convey friendliness, trus and memorability. Colors and everything else is up to you.

Target Market(s)

18-34 year old males and females

Industry/Entity Type

Business

```html
<!DOCTYPE html>
<html lang="en">
<head>
<meta charset="utf-8">
<title>Heron Lending — Business Card</title>
<link rel="stylesheet" href="https://fonts.googleapis.com/css2?family=Arimo:wght@400;700&display=swap">
<style>
  :root {
    --card-bg: #ffffff;
    --card-border: #9a9a9a;
    --brand-red: #ee1c24;
    --brand-blue: #2f6fd6;
    --tagline-blue: #4a86d8;
    --label-blue: #2a78d0;
    --mark-grey: #1c1c1c;
    --faint-grey: #e9eded;
  }
  * { margin: 0; padding: 0; box-sizing: border-box; }
  html, body {
    width: 1200px;
    height: 734px;
    overflow: hidden;
    background: var(--card-bg);
  }
  .card {
    position: relative;
    width: 1200px;
    height: 734px;
    background: var(--card-bg);
    border: 2px solid var(--card-border);
    font-family: "Arimo", Arial, sans-serif;
    overflow: hidden;
  }
  .backdrop-shape {
    position: absolute;
    left: 700px;
    top: 80px;
    width: 440px;
    height: 560px;
  }
  .brand {
    position: absolute;
    left: 44px;
    top: 28px;
    display: flex;
    align-items: center;
    gap: 22px;
  }
  .brand-dot {
    width: 110px;
    height: 110px;
    border-radius: 50%;
    background: var(--mark-grey);
    flex: none;
  }
  .brand-name {
    font-weight: 700;
    font-size: 64px;
    letter-spacing: 1px;
    color: var(--brand-red);
    text-transform: uppercase;
    line-height: 1;
  }
  .tagline {
    position: absolute;
    left: 214px;
    top: 128px;
    font-size: 31px;
    font-weight: 400;
    color: var(--tagline-blue);
  }
  .contact-fields {
    position: absolute;
    left: 60px;
    top: 372px;
    list-style: none;
  }
  .field {
    display: flex;
    align-items: baseline;
    font-size: 25px;
    font-weight: 700;
    color: var(--label-blue);
    height: 61px;
  }
  .field:nth-child(2) { height: 59px; }
  .field-label { white-space: nowrap; margin-right: 10px; }
  .field-line {
    display: block;
    border-bottom: 3px dotted var(--label-blue);
    height: 1px;
    align-self: center;
    transform: translateY(8px);
  }
</style>
</head>
<body>
  <main class="card">
    <svg class="backdrop-shape" viewBox="0 0 440 560" aria-hidden="true">
      <circle cx="230" cy="300" r="200" fill="var(--faint-grey)"/>
    </svg>

    <header class="brand">
      <span class="brand-dot" aria-hidden="true"></span>
      <span class="brand-name">Heron Lending</span>
    </header>
    <p class="tagline">car financing company</p>

    <ul class="contact-fields">
      <li class="field"><span class="field-label">Title:</span><span class="field-line" style="width:360px"></span></li>
      <li class="field"><span class="field-label">Name:</span><span class="field-line" style="width:350px"></span></li>
      <li class="field"><span class="field-label">address:</span><span class="field-line" style="width:325px"></span></li>
      <li class="field"><span class="field-label">phone number:</span><span class="field-line" style="width:210px"></span></li>
    </ul>
  </main>
</body>
</html>
```